R. K. Belvard & Associates, Inc

Gregor Belvard
Accountant
4219 NW 168th ST
Hialeah, Florida 33015
(305) 555-0187
greg.belvard@quillmarsh.com
Accounting - Tax Preparation Services - Bookkeeping
Side - one business logo on the left and business information on right
On Backside: The logo in the middle and under the logo my company name.

Rounded Corner of the cards
In reference to the logo and cards I need to adjust the circle around the RK and color.

```html
<!DOCTYPE html>
<html lang="en">
<head>
<meta charset="utf-8">
<title>R. K. Belvard &amp; Associates, Inc — Business Cards</title>
<link rel="stylesheet" href="https://fonts.googleapis.com/css2?family=Montserrat:wght@700&family=Roboto:wght@400;700&display=swap">
<style>
  :root {
    --backdrop: #222325;
    --brand-blue: #1a86c8;
    --brand-blue-light: #2aa0d6;
    --brand-blue-dark: #0f68b3;
    --ink: #2b2b2d;
    --paper: #ffffff;
    --muted: #333;
  }
  * { box-sizing: border-box; margin: 0; padding: 0; }
  html, body { width: 1200px; height: 929px; overflow: hidden; }
  body { background: var(--backdrop); position: relative; font-family: "Roboto", sans-serif; }

  .card {
    position: absolute;
    width: 700px;
    height: 400px;
    border-radius: 24px;
    overflow: hidden;
    box-shadow: 0 10px 30px rgba(0,0,0,.45);
  }

  .brand-name {
    position: absolute;
    display: flex; align-items: center; gap: 12px;
    font-family: "Montserrat", sans-serif; font-weight: 700;
    line-height: 1;
  }
  .brand-name__square { display: block; flex: none; }

  /* Back side */
  .card--back {
    left: 110px; top: 50px;
    background: linear-gradient(135deg, var(--brand-blue-dark) 0%, var(--brand-blue) 45%, var(--brand-blue-light) 100%);
  }
  .card--back .brand-name {
    left: 60px; top: 176px;
    font-size: 44px; color: var(--paper);
  }
  .card--back .brand-name__square { width: 26px; height: 26px; background: var(--paper); }
  .back__company {
    position: absolute; left: 340px; top: 118px;
    font-family: "Montserrat", sans-serif; font-weight: 700;
    color: var(--paper); font-size: 29px; line-height: 1.2;
    text-transform: uppercase;
  }
  .back__company span { display: block; }
  .back__company span + span { padding-left: 22px; }

  /* Front side */
  .card--front {
    left: 390px; top: 490px;
    background: var(--paper);
  }
  .card--front .brand-name {
    right: 60px; top: 96px;
    font-size: 34px; color: var(--ink);
  }
  .card--front .brand-name__square { width: 20px; height: 20px; background: var(--brand-blue); }
  .front__person {
    position: absolute; left: 52px; top: 205px;
  }
  .person__name {
    font-family: "Montserrat", sans-serif; font-weight: 700;
    font-size: 28px; color: var(--brand-blue); text-transform: uppercase;
    line-height: 1;
  }
  .person__role {
    font-family: "Roboto", sans-serif; font-weight: 700;
    font-size: 19px; color: var(--muted); margin-top: 4px; padding-left: 6px;
  }
  .person__rule {
    width: 30px; height: 3px; background: var(--brand-blue);
    margin: 14px 0 10px 18px;
  }
  .contact { list-style: none; padding-left: 18px; }
  .contact li {
    display: flex; align-items: center; gap: 8px;
    font-size: 19px; color: var(--muted); line-height: 1.4;
  }
  .contact svg { width: 18px; height: 18px; fill: var(--brand-blue); flex: none; }

  .front__address {
    position: absolute; right: 48px; top: 238px;
    text-align: right; font-size: 19px; line-height: 1.3; color: var(--muted);
    font-style: normal;
  }
  .front__services {
    position: absolute; left: 0; right: 0; bottom: 0; height: 58px;
    background: linear-gradient(90deg, var(--brand-blue-dark), var(--brand-blue));
    color: var(--paper);
    display: flex; align-items: center; justify-content: center;
    font-size: 20px; letter-spacing: 2.6px;
  }
</style>
</head>
<body>

<section class="card card--back" aria-label="Card back">
  <div class="brand-name"><span class="brand-name__square"></span>Belvard</div>
  <h1 class="back__company"><span>R. K. Belvard</span><span>&amp; Associates, Inc</span></h1>
</section>

<section class="card card--front" aria-label="Card front">
  <div class="brand-name"><span class="brand-name__square"></span>Belvard</div>

  <div class="front__person">
    <h2 class="person__name">Gregor Belvard</h2>
    <p class="person__role">Accountant</p>
    <div class="person__rule"></div>
    <ul class="contact">
      <li>
        <svg viewBox="0 0 24 24" aria-hidden="true"><path d="M6.6 10.8a15.1 15.1 0 0 0 6.6 6.6l2.2-2.2a1 1 0 0 1 1-.25 11.4 11.4 0 0 0 3.6.57 1 1 0 0 1 1 1V20a1 1 0 0 1-1 1A17 17 0 0 1 3 4a1 1 0 0 1 1-1h3.5a1 1 0 0 1 1 1c0 1.25.2 2.45.57 3.6a1 1 0 0 1-.25 1z"/></svg>
        (305) 555-0187
      </li>
      <li>
        <svg viewBox="0 0 24 24" aria-hidden="true"><path d="M2 5h20v14H2zm2 2v.4l8 5 8-5V7zm0 2.8V17h16V9.8l-8 5z"/></svg>
        greg.belvard@quillmarsh.com
      </li>
    </ul>
  </div>

  <address class="front__address">4219 NW 168th ST<br>Hialeah, Florida 33015</address>

  <p class="front__services">Accounting - Tax Preparation Services - Bookkeeping</p>
</section>

</body>
</html>
```